Mine Engineering Consultancy specializing in
* Pit optimization
* Mine Design
* Scheduling
* Mine Rehabilitation

Mining

RVT Mining Pty Ltd
Dennis Holloway
Director/Principle Mining Engineer
Mobile 0418263591
Email dennis.holloway@rvtmining-example.com

```html
<!DOCTYPE html>
<html lang="en">
<head>
<meta charset="utf-8">
<title>RVT Mining Pty Ltd – Business Card</title>
<link rel="stylesheet" href="https://fonts.googleapis.com/css2?family=Roboto:ital,wght@0,300;0,400;0,700;1,300&display=swap">
<style>
  :root {
    --stone-light: #bcbdbf;
    --stone-dark: #6d6e70;
    --brand-blue: #1a6fba;
    --name-grey: #b9babc;
    --white: #ffffff;
  }
  html, body {
    margin: 0;
    padding: 0;
    overflow: hidden;
    background: var(--white);
  }
  .card {
    position: relative;
    width: 1200px;
    height: 741px;
    overflow: hidden;
    background: var(--stone-light);
    font-family: "Roboto", Arial, sans-serif;
  }
  .card__shapes {
    position: absolute;
    inset: 0;
    width: 1200px;
    height: 741px;
  }
  .shape--dark { fill: var(--stone-dark); }
  .shape--blue { fill: var(--brand-blue); }

  .company-name {
    position: absolute;
    left: 102px;
    top: 590px;
    margin: 0;
    font-size: 44px;
    font-weight: 700;
    color: var(--brand-blue);
    white-space: nowrap;
  }

  .contact {
    position: absolute;
    left: 535px;
    top: 222px;
    color: var(--white);
  }
  .contact__name {
    margin: 0;
    font-size: 53px;
    font-weight: 700;
    line-height: 1;
    letter-spacing: 0.5px;
    text-transform: uppercase;
  }
  .contact__surname { color: var(--name-grey); }
  .contact__role {
    margin: 10px 0 0;
    font-size: 28px;
    font-weight: 300;
    line-height: 1.2;
  }
  .contact__details {
    margin: 38px 0 0;
    font-size: 28px;
    font-weight: 300;
    font-style: italic;
    line-height: 1.4;
  }
  .contact__details span { display: block; }
</style>
</head>
<body>
  <div class="card">
    <svg class="card__shapes" viewBox="0 0 1200 741" aria-hidden="true">
      <polygon class="shape--dark" points="168,0 768,0 368,301"/>
      <polygon class="shape--blue" points="768,0 1200,0 1200,741 649,741 368,301"/>
    </svg>

    <p class="company-name">RVT Mining Pty Ltd</p>

    <div class="contact">
      <h1 class="contact__name">Dennis <span class="contact__surname">Holloway</span></h1>
      <p class="contact__role">Director/Principle Mining Engineer</p>
      <p class="contact__details">
        <span class="contact__phone">0418263591</span>
        <span class="contact__email">dennis.holloway@rvtmining-example.com</span>
      </p>
    </div>
  </div>
</body>
</html>
```